Upmarket building and construction company needs signage

Our building company R Brent Construction, needs signage to put up on the side of our vehicle trailers and on site fencing. We are a building company that specialises in residential construction and carpentry .

I will attach our logo and some inspirational pics for site fencing as well as what our trailer looks like .
Other details i would like on the sign are our
( email) rbrentconstruction@mailbox-example.net
(mobile ) 0493 518 264
(website ) rbrentconstruction. example.net

Target Market(s)

Home owners looking for a reliable local builder who produces good quality work. I have attached some inspirational pics.

Industry/Entity Type

Building and Construction

Colors

Designer to choose colors to be used in the design.

Requirements
Must have
• Our logo, contact information
Nice to have
• We would like the design to have elements of being Elegant, Serious, Modern, Professional, Masculine, Conservative and Upmarket.

```html
<!DOCTYPE html>
<html lang="en">
<head>
<meta charset="UTF-8">
<title>R Brent Construction – Site Banner</title>
<link rel="stylesheet" href="https://fonts.googleapis.com/css2?family=Montserrat:wght@600;800&display=swap">
<style>
  :root {
    --backdrop: #e2e2e2;
    --band: #616161;
    --field: #f3f3f3;
    --ink: #5c5c5c;
    --band-text: #f7f7f7;
  }
  * { margin: 0; padding: 0; box-sizing: border-box; }
  html, body {
    width: 1200px;
    height: 988px;
    overflow: hidden;
    background: var(--backdrop);
  }
  .banner {
    position: absolute;
    left: 62px;
    top: 112px;
    width: 1076px;
    height: 764px;
    border-radius: 14px;
    overflow: hidden;
    background: var(--field);
    display: flex;
    flex-direction: column;
    font-family: "Montserrat", sans-serif;
  }
  .band {
    background: var(--band);
    color: var(--band-text);
    display: flex;
    flex-direction: column;
    align-items: center;
  }
  .band--phone {
    height: 140px;
    justify-content: center;
    font-weight: 800;
    font-size: 100px;
    letter-spacing: -1px;
    line-height: 1;
  }
  .band--contact {
    height: 155px;
    justify-content: flex-end;
    padding-bottom: 22px;
  }
  .contact__web {
    font-weight: 600;
    font-size: 26px;
    letter-spacing: 0.5px;
    margin-bottom: 14px;
  }
  .contact__email {
    font-weight: 800;
    font-size: 44px;
    letter-spacing: -0.5px;
    line-height: 1;
  }
  .brand {
    flex: 1;
    display: flex;
    align-items: center;
    justify-content: center;
  }
  .brand__name {
    color: var(--ink);
    font-weight: 800;
    font-size: 56px;
    line-height: 1.15;
    text-align: center;
    text-transform: uppercase;
  }
</style>
</head>
<body>
  <section class="banner">
    <div class="band band--phone">+61 493 518 264</div>
    <div class="brand">
      <h1 class="brand__name">R Brent<br>Construction</h1>
    </div>
    <div class="band band--contact">
      <p class="contact__web">rbrentconstruction.example.net</p>
      <p class="contact__email">rbrentconstruction@mailbox-example.net</p>
    </div>
  </section>
</body>
</html>
```